Advertisement Sign

Hello,
We're in need of a new design for an advertisement sign. Below is our current concept, but we're looking for improvements. Specifically, we'd like to enhance the size of the 'Call for Assistance' text, possibly explore different fonts, and possibly add a background to make the design more engaging and less plain. We need something that sticks out more. Any suggestions are welcome.

Target Market(s)

Construction and Landscape Companies

```html
<!DOCTYPE html>
<html lang="en">
<head>
<meta charset="utf-8">
<title>Kestrel Equipment Rentals – Roadside Sign</title>
<link rel="stylesheet" href="https://fonts.googleapis.com/css2?family=Krona+One&display=swap">
<style>
  :root {
    --canvas: #ffffff;
    --band-dark: #2b2a29;
    --panel-light: #ffffff;
    --brand-blue: #2c75bf;
    --text-white: #ffffff;
    --alert-red: #e31e24;
    --frame-line: #6d6d6d;
  }
  * { margin: 0; padding: 0; box-sizing: border-box; }
  html, body {
    width: 975px;
    height: 1200px;
    overflow: hidden;
    background: var(--canvas);
  }
  .canvas {
    position: relative;
    width: 975px;
    height: 1200px;
    background: var(--canvas);
  }
  .sign {
    position: absolute;
    left: 112px;
    top: 412px;
    width: 750px;
    height: 376px;
    border: 1px solid var(--frame-line);
    background: var(--panel-light);
    font-family: "Krona One", sans-serif;
    line-height: 1;
    white-space: nowrap;
  }
  .brand-band {
    position: absolute;
    left: 0;
    top: 0;
    width: 100%;
    height: 228px;
    background: var(--band-dark);
  }
  .brand-square {
    position: absolute;
    left: 92px;
    top: 62px;
    width: 62px;
    height: 62px;
    background: var(--brand-blue);
  }
  .brand-name {
    position: absolute;
    left: 212px;
    top: 42px;
    width: 486px;
    color: var(--text-white);
    font-size: 79px;
    letter-spacing: 0;
  }
  .brand-sub {
    position: absolute;
    left: 215px;
    top: 125px;
    color: var(--brand-blue);
    font-size: 21px;
    letter-spacing: 10.8px;
  }
  .tagline {
    position: absolute;
    left: 218px;
    top: 160px;
    width: 480px;
    display: flex;
    align-items: center;
    justify-content: space-between;
  }
  .tagline__rule { width: 82px; height: 3px; display: block; }
  .tagline__text {
    color: var(--text-white);
    font-size: 13px;
    letter-spacing: 2.4px;
  }
  .contact-call {
    position: absolute;
    left: 0;
    top: 248px;
    width: 100%;
    text-align: center;
    color: var(--alert-red);
    font-size: 33px;
    letter-spacing: 5.5px;
  }
  .contact-phone {
    position: absolute;
    left: 0;
    top: 298px;
    width: 100%;
    text-align: center;
    color: var(--alert-red);
    font-size: 57px;
    letter-spacing: 12px;
  }
</style>
</head>
<body>
  <main class="canvas">
    <section class="sign">
      <header class="brand-band">
        <span class="brand-square"></span>
        <p class="brand-name">KESTREL</p>
        <p class="brand-sub">EQUIPMENT RENTALS</p>
        <div class="tagline">
          <svg class="tagline__rule" viewBox="0 0 82 3" aria-hidden="true"><polygon points="0,1.5 82,0 82,3" fill="#ffffff"/></svg>
          <span class="tagline__text">BUILT FOR THE WORK</span>
          <svg class="tagline__rule" viewBox="0 0 82 3" aria-hidden="true"><polygon points="0,0 82,1.5 0,3" fill="#ffffff"/></svg>
        </div>
      </header>
      <p class="contact-call">CALL FOR ASSISTANCE</p>
      <p class="contact-phone">403-555-0148</p>
    </section>
  </main>
</body>
</html>
```